Lotus Harmony Massage Facebook Design Project

We need a design to our facebook page for a Thai Massage business located in Houston tx. The current website is lotusharmspa.example.
Target Market(s)
mostly middle aged from 30-50 25%women 75%men professionals from office to medical to retired
Industry/Entity Type
Business
Colors
Designer to choose colors to be used in the design.
Look and feel
Each slider illustrates characteristics of the customer's brand and the style your logo design should communicate.

```html
<!DOCTYPE html>
<html lang="en">
<head>
<meta charset="utf-8">
<title>Lotus Harmony Massage – Facebook Cover and Flyer</title>
<link rel="stylesheet" href="https://fonts.googleapis.com/css2?family=Libre+Baskerville:wght@400;700&family=Merriweather:ital,wght@0,700;1,900&display=swap">
<style>
  :root {
    --page: #ebe9e9;
    --bar: #2f5b9a;
    --panel: #fcfafb;
    --white: #ffffff;
    --brown-deep: #2a1406;
    --brown: #5a2a0a;
    --amber: #c9781c;
    --orange: #ef6a1a;
    --orange-soft: #f0822c;
    --gold: #f5b818;
    --gold-deep: #e39a10;
    --photo-light: #e8b04a;
  }
  * { margin: 0; padding: 0; box-sizing: border-box; }
  html, body { width: 1200px; height: 1000px; overflow: hidden; }
  body { background: var(--page); position: relative; font-family: "Merriweather", Georgia, serif; color: var(--white); }

  .top-bar { position: absolute; left: 0; top: 0; width: 1200px; height: 26px; background: var(--bar); }
  .page-panel { position: absolute; left: 63px; top: 26px; width: 966px; height: 404px; background: var(--panel); }

  .cover { position: absolute; left: 63px; top: 26px; width: 980px; height: 242px; overflow: hidden; background: var(--brown-deep); }
  .cover-photo { position: absolute; left: 0; top: 0; width: 640px; height: 242px;
    background: radial-gradient(ellipse at 55% 55%, var(--photo-light) 0%, var(--amber) 35%, var(--brown) 70%, var(--brown-deep) 100%); }
  .cover-blocks { position: absolute; left: 500px; top: 0; }

  .brand-name { font-family: "Libre Baskerville", Georgia, serif; font-weight: 700; color: var(--white); white-space: nowrap; line-height: 1; }
  .brand-tagline { font-family: "Libre Baskerville", Georgia, serif; font-weight: 400; color: var(--white); white-space: nowrap; line-height: 1; }

  .cover .brand-name { position: absolute; left: 18px; top: 22px; font-size: 34px; }
  .cover .brand-tagline { position: absolute; left: 62px; top: 54px; font-size: 14px; }

  .cta { font-family: "Libre Baskerville", Georgia, serif; font-weight: 400; color: var(--white); line-height: 1; text-shadow: 2px 2px 2px rgba(0,0,0,.55); position: absolute; white-space: nowrap; }
  .cover .cta-contact { left: 625px; top: 24px; font-size: 38px; letter-spacing: 1px; }
  .cover .cta-us { left: 792px; top: 77px; font-size: 23px; }
  .cover .cta-today { left: 597px; top: 100px; font-size: 62px; }

  .contact-lines { position: absolute; font-weight: 700; color: var(--white); white-space: nowrap; text-shadow: 1px 1px 1px rgba(0,0,0,.5); }
  .cover .contact-lines { left: 709px; top: 171px; font-size: 12px; line-height: 14px; }

  .profile-thumb { position: absolute; left: 108px; top: 230px; width: 225px; height: 109px; border: 3px solid var(--white); overflow: hidden;
    background: radial-gradient(ellipse at 60% 60%, var(--photo-light) 0%, var(--amber) 40%, var(--brown) 75%, var(--brown-deep) 100%); }
  .profile-thumb .brand-name { position: absolute; left: 8px; top: 9px; font-size: 16px; }
  .profile-thumb .brand-tagline { position: absolute; left: 30px; top: 25px; font-size: 7px; }

  .flyer { position: absolute; left: 553px; top: 442px; width: 470px; height: 470px; overflow: hidden; background: var(--brown-deep); }
  .flyer-photo { position: absolute; left: 0; top: 0; width: 470px; height: 226px;
    background: radial-gradient(ellipse at 50% 62%, var(--photo-light) 0%, var(--amber) 35%, var(--brown) 72%, var(--brown-deep) 100%); }
  .flyer-blocks { position: absolute; left: 0; top: 226px; }
  .flyer .brand-name { position: absolute; left: 12px; top: 24px; font-size: 36px; }
  .flyer .brand-tagline { position: absolute; left: 56px; top: 61px; font-size: 16px; }

  .services { position: absolute; left: 176px; top: 240px; width: 285px; text-shadow: 1px 1px 1px rgba(0,0,0,.5); }
  .services-title { font-size: 13px; font-weight: 700; margin-bottom: 14px; }
  .services-list { list-style: none; font-style: italic; font-weight: 900; font-size: 12.5px; line-height: 13px; letter-spacing: .7px; }
  .services-list span { display: inline-block; width: 33px; padding-left: 2px; }

  .flyer .cta { text-align: center; width: 120px; left: 10px; }
  .flyer .cta-contact { top: 356px; font-size: 18px; }
  .flyer .cta-us { top: 375px; font-size: 18px; }
  .flyer .cta-today { top: 394px; font-size: 21px; }
  .flyer .contact-lines { left: 13px; top: 418px; font-size: 11px; line-height: 12px; font-weight: 400; font-family: "Libre Baskerville", Georgia, serif; }
  .flyer .contact-lines .email { margin-top: 2px; display: block; }

  .rates { position: absolute; left: 240px; top: 418px; font-family: "Libre Baskerville", Georgia, serif; font-size: 11px; line-height: 11px; border-collapse: collapse; text-shadow: 1px 1px 1px rgba(0,0,0,.4); }
  .rates th { font-weight: 400; padding: 0 0 1px 0; }
  .rates td { padding: 0; white-space: nowrap; }
  .rates .mins { padding-left: 4px; width: 86px; }
</style>
</head>
<body>
  <div class="top-bar"></div>
  <div class="page-panel"></div>

  <section class="cover">
    <div class="cover-photo" role="img" aria-label="Photo of a smiling woman relaxing on a massage table while receiving a shoulder massage, warm amber light"></div>
    <svg class="cover-blocks" width="480" height="242" viewBox="0 0 480 242" aria-hidden="true">
      <defs>
        <linearGradient id="fadeLeft" x1="0" x2="1"><stop offset="0" stop-color="#2a1406" stop-opacity="1"/><stop offset=".3" stop-color="#2a1406" stop-opacity="0"/></linearGradient>
      </defs>
      <rect x="50" y="0" width="300" height="20" fill="var(--orange)"/>
      <rect x="350" y="0" width="130" height="20" fill="var(--gold-deep)"/>
      <rect x="80" y="40" width="180" height="75" fill="var(--orange-soft)"/>
      <rect x="200" y="30" width="170" height="35" fill="var(--gold)"/>
      <rect x="260" y="65" width="220" height="30" fill="var(--gold-deep)"/>
      <rect x="370" y="40" width="110" height="60" fill="var(--gold)"/>
      <rect x="100" y="130" width="170" height="55" fill="var(--orange)"/>
      <rect x="270" y="120" width="130" height="40" fill="var(--orange-soft)"/>
      <rect x="400" y="150" width="80" height="50" fill="var(--gold)"/>
      <rect x="180" y="195" width="200" height="47" fill="var(--orange)"/>
      <rect x="380" y="205" width="100" height="37" fill="var(--gold-deep)"/>
      <rect x="0" y="0" width="480" height="242" fill="url(#fadeLeft)"/>
    </svg>
    <div class="brand-name">Lotus Harmony</div>
    <div class="brand-tagline">“Massage Professionals”</div>
    <div class="cta cta-contact">CONTACT</div>
    <div class="cta cta-us">US</div>
    <div class="cta cta-today">TODAY!</div>
    <address class="contact-lines" style="font-style:normal">
      1450 Willow Bend Dr.<br>
      Houston TX 77006<br>
      (713)555-0142<br>
      info@lotusharmspa.example
    </address>
  </section>

  <div class="profile-thumb">
    <div class="brand-name">Lotus Harmony</div>
    <div class="brand-tagline">“Massage Professionals”</div>
  </div>

  <section class="flyer">
    <div class="flyer-photo" role="img" aria-label="Photo of a smiling woman relaxing on a massage table while receiving a shoulder massage, warm amber light"></div>
    <svg class="flyer-blocks" width="470" height="244" viewBox="0 0 470 244" aria-hidden="true">
      <rect x="0" y="0" width="470" height="244" fill="#3a1a06"/>
      <rect x="0" y="4" width="120" height="44" fill="var(--gold-deep)"/>
      <rect x="120" y="14" width="200" height="40" fill="var(--orange)"/>
      <rect x="320" y="4" width="150" height="44" fill="var(--gold)"/>
      <rect x="0" y="60" width="60" height="50" fill="var(--gold)"/>
      <rect x="60" y="70" width="180" height="40" fill="var(--orange-soft)"/>
      <rect x="240" y="56" width="230" height="44" fill="var(--gold-deep)"/>
      <rect x="0" y="125" width="200" height="45" fill="var(--gold)"/>
      <rect x="200" y="118" width="150" height="40" fill="var(--orange)"/>
      <rect x="350" y="128" width="120" height="50" fill="var(--gold)"/>
      <rect x="0" y="180" width="230" height="64" fill="var(--gold-deep)"/>
      <rect x="230" y="190" width="130" height="54" fill="var(--orange)"/>
      <rect x="360" y="185" width="110" height="59" fill="var(--gold)"/>
    </svg>
    <div class="brand-name">Lotus Harmony</div>
    <div class="brand-tagline">“Massage Professionals”</div>

    <div class="services">
      <h2 class="services-title">Our Services</h2>
      <ol class="services-list">
        <li><span>1.</span>Combination Massage</li>
        <li><span>2.</span>Thai Traditional Massage</li>
        <li><span>3.</span>Thai Healing Massage</li>
        <li><span>4.</span>Back, Head and Shoulder Massage</li>
        <li><span>5.</span>Thai Aromatherapy Body Massage</li>
        <li><span>6.</span>Swedish &amp; Shiatsu Massage</li>
        <li><span>7.</span>Couple Massage</li>
        <li><span>8.</span>Chinese Medicine Massage</li>
      </ol>
    </div>

    <div class="cta cta-contact">CONTACT</div>
    <div class="cta cta-us">US</div>
    <div class="cta cta-today">TODAY!</div>
    <address class="contact-lines" style="font-style:normal">
      1450 Willow Bend Dr.<br>
      Houston TX 77006<br>
      (713)555-0142
      <span class="email">info@lotusharmspa.example</span>
    </address>

    <table class="rates">
      <tr><th colspan="2">Duration&nbsp;&nbsp;&nbsp;&nbsp;/&nbsp;&nbsp;&nbsp;&nbsp;Rate</th></tr>
      <tr><td class="mins">60&nbsp;&nbsp;&nbsp;mins</td><td>$80/person</td></tr>
      <tr><td class="mins">90&nbsp;&nbsp;&nbsp;mins</td><td>$120/person</td></tr>
      <tr><td class="mins">120&nbsp;mins</td><td>$160/person</td></tr>
    </table>
  </section>
</body>
</html>
```